Unternehmensvorstellung : Broschüre DIN A4 ca. 6 Innenseiten.
Zielgruppe
Dienstleistungen:
- Messdienst und Erstellung Heiz- und Nebenkostenabrechung für Mieter
- Rauchwarnmelder Montage und Wartung
- Trinkwasser/Legionellenprüfung
- Energie-Monitoring-Service (automatisch Ermittlung günstigster Versorger)
Für:
Immobilienverwalter
Immobilienbesitzer
Immobilien Gesellschaften
Architekten und Planer
Aufgabenstellung
siehe Homepage www.wohnarcaplus.de

```html
<!DOCTYPE html>
<html lang="de">
<head>
<meta charset="utf-8">
<title>WOHNARCAplus Imagebroschüre – Seite 08/09</title>
<link href="https://fonts.googleapis.com/css2?family=Barlow:wght@400;500;600&display=swap" rel="stylesheet">
<style>
  :root {
    --brand-blue: #0a82c8;
    --title-blue: #1a7dc0;
    --text: #3c3c3c;
    --text-dark: #222;
    --page-grey: #f2f2f2;
    --tick-green: #7ab929;
    --tick-red: #e24a2a;
    --tick-blue: #1a7fc6;
  }
  * { box-sizing: border-box; margin: 0; padding: 0; }
  html, body { width: 1200px; height: 424px; overflow: hidden; background: #fff; }
  body { font-family: "Barlow", Arial, sans-serif; color: var(--text); position: relative; }
  .spread-art { position: absolute; inset: 0; }
  .abs { position: absolute; }

  .page-tab {
    position: absolute; top: 21px; height: 9px; width: 30px;
    background: var(--brand-blue); color: #fff; font-size: 4px;
    display: flex; align-items: center; justify-content: center;
  }
  .running-head { top: 23px; left: 36px; font-size: 4px; color: var(--text-dark); }
  .running-head b { font-weight: 600; }

  .page-title {
    font-size: 16px; font-weight: 600; color: var(--title-blue); letter-spacing: 0.2px;
  }
  .copy { font-size: 6.6px; line-height: 10px; text-align: justify; }
  .copy-q { font-size: 6.6px; line-height: 10px; font-weight: 600; color: var(--text-dark); }
  .copy-label { font-size: 6.6px; line-height: 10px; text-transform: uppercase; }

  .service-list { list-style: none; }
  .service-list li {
    position: absolute; left: 0; font-size: 6.6px; line-height: 7px;
    padding-left: 15px; display: flex; align-items: center;
  }
  .service-list li svg { position: absolute; left: 0; top: 50%; transform: translateY(-50%); }
  .overview-head { font-size: 6.8px; font-weight: 600; color: var(--text-dark); letter-spacing: 0.2px; }
</style>
</head>
<body>
  <svg class="spread-art" width="1200" height="424" viewBox="0 0 1200 424">
    <defs>
      <linearGradient id="detectorTone" x1="0" y1="0" x2="0" y2="1">
        <stop offset="0" stop-color="#c9ced2"/>
        <stop offset="0.35" stop-color="#e3e5e6"/>
        <stop offset="0.6" stop-color="#f4f4f3"/>
        <stop offset="0.9" stop-color="#f1eeea"/>
        <stop offset="1" stop-color="#d9cfc4"/>
      </linearGradient>
      <linearGradient id="waterTone" x1="0" y1="0" x2="1" y2="1">
        <stop offset="0" stop-color="#f6f8f9"/>
        <stop offset="0.5" stop-color="#dfe6ea"/>
        <stop offset="1" stop-color="#b9c4cb"/>
      </linearGradient>
    </defs>
    <rect x="600" y="0" width="360" height="424" fill="var(--page-grey)"/>
    <polygon role="img" aria-label="Foto: Rauchwarnmelder an der Zimmerdecke" points="0,0 201,0 273,424 0,424" fill="url(#detectorTone)"/>
    <polygon points="201,0 225,0 299,424 273,424" fill="var(--brand-blue)"/>
    <polygon role="img" aria-label="Foto: Wasser wird aus einer Karaffe in ein Glas gegossen" points="970,0 1200,0 1200,424 898,424" fill="url(#waterTone)"/>
    <polygon points="954,0 970,0 898,424 880,424" fill="var(--brand-blue)"/>
  </svg>

  <!-- Seite 08 -->
  <div class="page-tab" style="left:0">Seite 08</div>
  <div class="abs running-head"><b>WOHNARCAplus</b> MESSDIENST SERVICE IMAGEBROSCHÜRE</div>

  <h2 class="abs page-title" style="right:631px; top:44px;">Rauchwarnmelder-Service</h2>

  <p class="abs copy" style="left:280px; width:289px; top:86px;">Rauchwarnmelder, Hitzemelder und CO-Melder. Wir informieren und beraten Sie gerne auch Persönlich über die Rauchwarnmelder und Rauchwarnmelderpflicht.</p>
  <p class="abs copy" style="left:285px; width:284px; top:116px;">WOHNARCAplus ist Ihr kompetenter Partner von der persönlichen Beratung, der Vorortbesichtigung über die Installation und Wartung bis hin zur Archivierung der Dokumentaion der Installation und Wartung - natürlich auch mit KORAL.</p>
  <p class="abs copy-label" style="left:292px; top:155px;">Einige Fragen und Antworten</p>
  <p class="abs copy-q" style="left:293px; top:165px;">Wie groß ist die Gefahr durch Brände in privaten Haushalten?</p>
  <p class="abs copy" style="left:296px; width:273px; top:179px;">500 Brandtote und rund 50.000 Verletzte: Das ist der jährliche Durchschnitt deutscher Brandopfer. Die lebensrettende Ausstattung mit Rauchwarnmeldern findet gerade einmal in 20-30 Prozent der deutschen Haushalte statt. Höchste Zeit also für eine gesetzliche Ausstattungspflicht. In zehn Bundesländern gibt es diese bereits für Neu- und Umbauten. Die Nachrüstpflicht für Bestandsbauten ist bereits in sieben von diesen Bundesländern zu einem bestimmten Zeitpunkt verpflichtend. Wir können nur jedem empfehlen seine Wohnung mit Rauchwarnmeldern auszustatten, denn Rauchwarnmelder retten Leben.</p>
  <p class="abs copy-q" style="left:311px; top:269px;">In welchen Räumen sollte man einen Rauchwarnmelder montieren?</p>
  <p class="abs copy" style="left:313px; width:256px; top:283px;">In der Anwendungsnorm DIN 14676 steht es sollen Schlaf- und Kinderzimmer sowie Flure, die als Rettungsweg dienen, ausgestattet werden. Wir empfehlen grundsätzlich eine optimale Ausstattung, also die Ausstattung aller Räume mit Ausnahme von Küchen und Bädern</p>
  <p class="abs copy-q" style="left:321px; top:333px;">Muss ein Rauchwarnmelder unbedingt immer an der Decke befestigt werden?</p>
  <p class="abs copy" style="left:324px; width:245px; top:347px;">Ja, denn der Rauch steigt nach oben und konzentriert sich genau dort. An Dachschrägen und an schrägen Wänden (Generell ist alles in der DIN 14676 geregel) sind auch Anordnungen mit besonderen Raumgeometrien berücksichtigt (Eckbereiche, rechtwinkliger Flur oder Gang, Dachschrägen, schräge Wände etc.).</p>

  <h3 class="abs overview-head" style="left:30px; top:253px;">RAUCHWARNMELDER-SERVICE LEISTUNGSÜBERSICHT</h3>
  <ul class="abs service-list" style="left:30px; top:0; width:220px;">
    <li style="top:271px; line-height:6px;"><svg width="9" height="9" viewBox="0 0 9 9"><rect width="9" height="9" rx="1" fill="var(--tick-green)"/><path d="M2 4.6l1.8 1.8L7 3" stroke="#fff" stroke-width="1.2" fill="none"/></svg>Q-Label zertifiziert Produkte nach DIN 14604 für Bereiche<br>nach DIN 14676</li>
    <li style="top:291px;"><svg width="9" height="9" viewBox="0 0 9 9"><rect width="9" height="9" rx="1" fill="var(--tick-green)"/><path d="M2 4.6l1.8 1.8L7 3" stroke="#fff" stroke-width="1.2" fill="none"/></svg>Q-Geprüfte Fachkräfte für Rauchwarnmelder nach DIN 14676</li>
    <li style="top:306px;"><svg width="9" height="9" viewBox="0 0 9 9"><rect width="9" height="9" rx="1" fill="var(--tick-green)"/><path d="M2 4.6l1.8 1.8L7 3" stroke="#fff" stroke-width="1.2" fill="none"/></svg>Persönliche Beratung</li>
    <li style="top:322px;"><svg width="9" height="9" viewBox="0 0 9 9"><rect width="9" height="9" rx="1" fill="var(--tick-green)"/><path d="M2 4.6l1.8 1.8L7 3" stroke="#fff" stroke-width="1.2" fill="none"/></svg>Vorortbesichtigung</li>
    <li style="top:337px;"><svg width="9" height="9" viewBox="0 0 9 9"><rect width="9" height="9" rx="1" fill="var(--tick-green)"/><path d="M2 4.6l1.8 1.8L7 3" stroke="#fff" stroke-width="1.2" fill="none"/></svg>Installation der Rauchwarnmelder, Hitzemelder und CO-Melder</li>
    <li style="top:352px;"><svg width="9" height="9" viewBox="0 0 9 9"><rect width="9" height="9" rx="1" fill="var(--tick-green)"/><path d="M2 4.6l1.8 1.8L7 3" stroke="#fff" stroke-width="1.2" fill="none"/></svg>Wartung mit KORAL</li>
    <li style="top:368px;"><svg width="9" height="9" viewBox="0 0 9 9"><rect width="9" height="9" rx="1" fill="var(--tick-green)"/><path d="M2 4.6l1.8 1.8L7 3" stroke="#fff" stroke-width="1.2" fill="none"/></svg>Archivierung mit KORAL</li>
  </ul>

  <!-- Seite 09 -->
  <div class="page-tab" style="left:1170px">Seite 09</div>

  <h2 class="abs page-title" style="left:631px; top:44px;">Trinkwasser-Service-Legionellenprüfung</h2>

  <p class="abs copy" style="left:630px; width:269px; top:86px;">Legionellenprüfung und Probestellenerrichtung. Wir informieren und beraten Sie gerne auch Persönlich über die novellierte Trinkwasserverordnung und führen bei Bedarf, die von der gesetzlichen Trinkwasserverordnung vorgeschriebenen Legionellenprüfung durch, zumdem errichten wir gegebenenfalls in Ihrem Gebäude, Ihrer Liegenschaft die Probenahmenstellen.</p>
  <p class="abs copy" style="left:630px; width:258px; top:146px;">WOHNARCAplus ist Ihr kompetenter Partner von der persönlichen Beratung, der Vorortbesichtigung über die Installation von Probenahmestellen, der Probenahme und Untersuchung bis hin zur Abwicklung mit den Behörden und der Archivierung - natürlich auch mit KORAL.</p>
  <p class="abs copy" style="left:630px; width:250px; top:196px;">Wenn Sie bis jetzt noch nicht gehandelt haben, sollten Sie dies schnellst möglich tun, denn die Abgabefrist für den Legionellenprüfbericht beim zuständigen Gesundheitsamt läuft zum 31.12.2013 ab.</p>
  <p class="abs copy" style="left:630px; width:245px; top:235px;">Weitere Informationen und einigen häufig gestellten Fragen und Antworten (FAQ) finden Sie auf unserer Internetseite www.wohnarcaplus.de.</p>

  <h3 class="abs copy" style="left:630px; top:269px; font-weight:400;">Trinkwasser-Service Leistungsübersicht</h3>
  <ul class="abs service-list" style="left:630px; top:0; width:240px;">
    <li style="top:287px;"><svg width="9" height="9" viewBox="0 0 9 9"><rect width="9" height="9" rx="1" fill="var(--tick-red)"/><path d="M2 4.6l1.8 1.8L7 3" stroke="#fff" stroke-width="1.2" fill="none"/></svg>Persönliche Beratung</li>
    <li style="top:300px;"><svg width="9" height="9" viewBox="0 0 9 9"><rect width="9" height="9" rx="1" fill="var(--tick-blue)"/><path d="M2 4.6l1.8 1.8L7 3" stroke="#fff" stroke-width="1.2" fill="none"/></svg>Vorortbesichtigung</li>
    <li style="top:313px;"><svg width="9" height="9" viewBox="0 0 9 9"><rect width="9" height="9" rx="1" fill="var(--tick-red)"/><path d="M2 4.6l1.8 1.8L7 3" stroke="#fff" stroke-width="1.2" fill="none"/></svg>Installation von Probeentnahmestellen</li>
    <li style="top:326px;"><svg width="9" height="9" viewBox="0 0 9 9"><rect width="9" height="9" rx="1" fill="var(--tick-blue)"/><path d="M2 4.6l1.8 1.8L7 3" stroke="#fff" stroke-width="1.2" fill="none"/></svg>Probenahmen mit KORAL</li>
    <li style="top:339px;"><svg width="9" height="9" viewBox="0 0 9 9"><rect width="9" height="9" rx="1" fill="var(--tick-red)"/><path d="M2 4.6l1.8 1.8L7 3" stroke="#fff" stroke-width="1.2" fill="none"/></svg>Untersuchung auf Legionellen</li>
    <li style="top:352px;"><svg width="9" height="9" viewBox="0 0 9 9"><rect width="9" height="9" rx="1" fill="var(--tick-blue)"/><path d="M2 4.6l1.8 1.8L7 3" stroke="#fff" stroke-width="1.2" fill="none"/></svg>Abwicklung mit den Behörden evtl. Maßnahmen</li>
    <li style="top:365px;"><svg width="9" height="9" viewBox="0 0 9 9"><rect width="9" height="9" rx="1" fill="var(--tick-red)"/><path d="M2 4.6l1.8 1.8L7 3" stroke="#fff" stroke-width="1.2" fill="none"/></svg>Archivierung mit KORAL</li>
  </ul>
</body>
</html>
```